Calvoterra business card

a nice business card with the logo,
Calvoterra
Teresa Lindqvist
Marketing Director
CH-1563 Geneva
Switzerland
+41 76 382 1904
email: Teresa.Lindqvist@calvoterra-mail.example

Target Market(s)

fertilizer business people, very nice and classic business card, normal size, make it nice and funky, try to make it different from the normal boring ones if possible.

Industry/Entity Type

Farming

Number of Pages Required

1 page

Requirements
Must have
• logo, Calvoterra, my name - mail and phone number
regular business card size for me to print easy please

```html
<!DOCTYPE html>
<html lang="en">
<head>
<meta charset="utf-8">
<title>Calvoterra business card</title>
<link href="https://fonts.googleapis.com/css2?family=Arimo:wght@400;700&display=swap" rel="stylesheet">
<style>
  :root {
    --page: #ffffff;
    --card: #ffffff;
    --card-edge: #3a3a3a;
    --band: #636466;
    --band-deep: #4d4e50;
    --brand-grey: #6d6e70;
    --leaf-green: #a8cd3a;
    --ink: #111111;
  }
  html, body {
    margin: 0;
    padding: 0;
    width: 882px;
    height: 1200px;
    overflow: hidden;
    background: var(--page);
  }
  .canvas {
    position: relative;
    width: 882px;
    height: 1200px;
    font-family: "Arimo", Arial, sans-serif;
  }
  .card {
    position: absolute;
    left: 128px;
    top: 89px;
    width: 649px;
    height: 1003px;
    background: var(--card);
    border: 1px solid var(--card-edge);
    box-sizing: border-box;
    box-shadow: 12px 14px 22px rgba(0, 0, 0, 0.22);
    overflow: hidden;
  }
  .side-band {
    position: absolute;
    left: 0;
    top: 0;
    width: 105px;
    height: 100%;
    background: var(--band);
  }
  .side-band__motif {
    position: absolute;
    left: 0;
    bottom: 0;
    width: 105px;
    height: 355px;
    background: linear-gradient(180deg, var(--band) 0%, var(--band-deep) 55%, var(--band) 100%);
  }
  .brand {
    position: absolute;
    left: 148px;
    top: 60px;
  }
  .brand__dot {
    position: absolute;
    left: 72px;
    top: 100px;
    width: 124px;
    height: 124px;
    border-radius: 50%;
    background: var(--leaf-green);
  }
  .brand__name {
    position: absolute;
    left: 0;
    top: 346px;
    margin: 0;
    font-weight: 700;
    font-size: 22px;
    line-height: 1;
    letter-spacing: 0.46em;
    color: var(--brand-grey);
    white-space: nowrap;
  }
  .person {
    position: absolute;
    left: 148px;
    top: 585px;
  }
  .person__name {
    margin: 0;
    font-weight: 400;
    font-size: 40px;
    line-height: 48px;
    color: var(--leaf-green);
    white-space: nowrap;
  }
  .person__role {
    margin: 4px 0 0;
    font-weight: 400;
    font-size: 33px;
    line-height: 40px;
    color: var(--ink);
    white-space: nowrap;
  }
  .contact {
    position: absolute;
    left: 148px;
    top: 776px;
    margin: 0;
    font-style: normal;
    font-size: 28px;
    line-height: 40.5px;
    color: var(--ink);
  }
  .contact span { display: block; white-space: nowrap; }
  .contact__email { font-size: 23px; }
</style>
</head>
<body>
<div class="canvas">
  <div class="card">
    <div class="side-band">
      <div class="side-band__motif" role="img" aria-label="Decorative wave motif in darker grey"></div>
    </div>

    <div class="brand">
      <div class="brand__dot"></div>
      <p class="brand__name">CALVOTERRA</p>
    </div>

    <div class="person">
      <h1 class="person__name">Teresa Lindqvist</h1>
      <p class="person__role">Marketing Director</p>
    </div>

    <address class="contact">
      <span>CH-1563 Geneva</span>
      <span>Switzerland</span>
      <span>+41 76 382 1904</span>
      <span class="contact__email">Teresa.Lindqvist@calvoterra-mail.example</span>
    </address>
  </div>
</div>
</body>
</html>
```